Northwind Trade Allies - Letterhead and Folder

I am looking for letterhead that uses the splash from the logo on the side of the page as well as some information from our website.

I am looking for a folder that is a fold out that has pockets to hold paper as well as a slits for a business card.

Website address is www.northwindtradeallies.example

Target Market(s)

Export of Agrifoods, commodities and emergency aid.
Supplying the world food security.

Requirements
Must have
• Use splash and logo, have information about company.
• Letterhead must have splash on a side not in the middle.
Nice to have
• Different pictures that what are provided.

```html
<!DOCTYPE html>
<html lang="en">
<head>
<meta charset="utf-8">
<title>Northwind Trade Allies – Letterhead</title>
<link href="https://fonts.googleapis.com/css2?family=Arimo:wght@400;700&display=swap" rel="stylesheet">
<style>
  :root {
    --backdrop: #efefef;
    --paper: #ffffff;
    --ink: #3a3a3a;
    --green-deep: #3f9a3c;
    --green-fresh: #93b824;
    --wash-blue: #dbe8ec;
    --wash-green: #e4eedf;
  }
  * { box-sizing: border-box; margin: 0; padding: 0; }
  html, body {
    width: 1200px; height: 795px; overflow: hidden;
    background: var(--backdrop);
    font-family: "Arimo", Arial, sans-serif;
    color: var(--ink);
  }
  .letterhead {
    position: absolute;
    left: 335px; top: 22px;
    width: 530px; height: 750px;
    background: var(--paper);
    box-shadow: 0 2px 10px rgba(0,0,0,0.12);
    overflow: hidden;
  }
  .letterhead__art { position: absolute; inset: 0; width: 100%; height: 100%; }
  .brand {
    position: absolute; left: 120px; top: 62px;
    display: flex; align-items: center; gap: 10px;
  }
  .brand__dot {
    width: 26px; height: 26px; border-radius: 50%;
    background: var(--green-deep);
  }
  .brand__name {
    font-size: 13px; font-weight: 700; letter-spacing: 0.08em;
    text-transform: uppercase; color: var(--ink);
  }
  .contact {
    position: absolute; left: 124px; top: 512px;
    font-size: 9px; line-height: 13px; font-style: normal;
  }
  .contact__address { margin-bottom: 6px; padding-left: 16px; }
  .contact__list { list-style: none; }
  .contact__item { display: flex; align-items: center; gap: 8px; }
  .contact__icon { width: 8px; height: 8px; flex: none; }
  .contact__icon * { fill: none; stroke: var(--green-deep); stroke-width: 1.3; }
</style>
</head>
<body>
<main class="letterhead">
  <svg class="letterhead__art" viewBox="0 0 530 750">
    <defs>
      <radialGradient id="wash" cx="0.6" cy="0.6" r="0.6">
        <stop offset="0" stop-color="var(--wash-blue)"/>
        <stop offset="1" stop-color="var(--wash-green)" stop-opacity="0"/>
      </radialGradient>
    </defs>
    <rect class="brand-wash" role="img" aria-label="Faint brand splash decoration area"
          x="370" y="420" width="160" height="190" fill="url(#wash)"/>
    <path class="sweep-deep" fill="var(--green-deep)"
          d="M530 420 C 498 458, 480 528, 484 606 L530 596 Z"/>
    <path class="sweep-fresh" fill="var(--green-fresh)"
          d="M60 750 C 200 660, 380 610, 530 595 L530 750 Z"/>
  </svg>

  <header class="brand">
    <span class="brand__dot"></span>
    <span class="brand__name">Northwind Trade Allies</span>
  </header>

  <address class="contact">
    <div class="contact__address">
      Unit 7, 18 Harrowfield Lane<br>
      Millbank Quarter<br>
      Leeds LS9 4QT
    </div>
    <ul class="contact__list">
      <li class="contact__item">
        <svg class="contact__icon" viewBox="0 0 8 8"><path d="M1.5 1 h1.5 l0.5 1.5 -1 0.8 a4 4 0 0 0 1.7 1.7 l0.8 -1 1.5 0.5 v1.5 a1 1 0 0 1 -1 1 A6 6 0 0 1 0.5 2 a1 1 0 0 1 1 -1z"/></svg>
        +44 (0)113 555 0148
      </li>
      <li class="contact__item">
        <svg class="contact__icon" viewBox="0 0 8 8"><rect x="2" y="0.7" width="4" height="6.6" rx="0.6"/></svg>
        +44 (0)7700 900 362
      </li>
      <li class="contact__item">
        <svg class="contact__icon" viewBox="0 0 8 8"><rect x="0.7" y="1.5" width="6.6" height="5"/><path d="M0.7 1.5 L4 4.3 L7.3 1.5"/></svg>
        hello@northwindtradeallies.example
      </li>
      <li class="contact__item">
        <svg class="contact__icon" viewBox="0 0 8 8"><circle cx="4" cy="4" r="3.3"/><path d="M0.7 4 h6.6 M4 0.7 c-2 2 -2 4.6 0 6.6 c2 -2 2 -4.6 0 -6.6"/></svg>
        www.northwindtradeallies.example
      </li>
    </ul>
  </address>
</main>
</body>
</html>
```